Pool Services Flyer promote regular pool services

We need a flyer design to be send out as a DL Postcard

We are a pool and spa maintenance business and would like to promote of regular pool services.
Please see our website www.brightripplepoolcare.com.au and our facebook page https://www.facebook.com/pages/Bright-Ripple-Pool-Care/583920174630518

We are pretty flexible with layouts etc Our monthly pool service is $67.00 plus chemicals so we would like this highlighted on our ad. We also so one off, weekly and fortnightly services as well.

We would like our details and logo on front and website also listed.

Target Market(s)

Pool owners

Industry/Entity Type

Pool Service

Colors
33a6d7
0292cd
0555a3
3276b5
85abd2

Requirements
Must have
• Logo
• website address
• phone number
• Price
• Promote the fact that customer wont have to worry about their pool
Nice to have
• like to have a blue wave down the bottom of flyer witht eh contact information in it. Would like to to be crisp not over crowed with information

```html
<!DOCTYPE html>
<html lang="en">
<head>
<meta charset="utf-8">
<title>Bright Ripple Pool Care – Monthly Pool Service Postcard</title>
<link href="https://fonts.googleapis.com/css2?family=Open+Sans:wght@400;600;700&display=swap" rel="stylesheet">
<style>
  :root {
    --sky-blue: #33a6d7;
    --brand-blue: #0292cd;
    --deep-blue: #0555a3;
    --mid-blue: #3276b5;
    --soft-blue: #85abd2;
    --headline-blue: #1a78bf;
    --ink: #2b2b2b;
    --green-dark: #0c7f36;
    --green-light: #22a64c;
    --price-red: #e0261c;
    --white: #ffffff;
  }
  * { margin: 0; padding: 0; box-sizing: border-box; }
  html, body { width: 1200px; height: 572px; overflow: hidden; background: var(--white); }
  body { font-family: "Open Sans", Arial, sans-serif; }

  .postcard { position: relative; width: 1200px; height: 572px; overflow: hidden; background: var(--white); }

  .scene-hillside {
    position: absolute; left: 0; top: 0; width: 580px; height: 572px;
    background: linear-gradient(180deg, #dfe9ee 0%, #c9d6cf 45%, #9fb48f 75%, #7d9a6a 100%);
  }
  .scene-pool {
    position: absolute; left: 578px; top: 0; width: 622px; height: 572px;
    background:
      linear-gradient(180deg, #cfe8f6 0%, #b9dcef 18%, #d9c6a4 30%, #e6d3b2 42%, transparent 46%),
      linear-gradient(180deg, #5ed0ee 46%, #2fbde6 70%, #17a7da 100%);
  }

  .intro-panel {
    position: absolute; left: 47px; top: 29px; width: 532px; height: 446px;
    background: rgba(255, 255, 255, 0.72);
  }

  .top-band, .bottom-wave { position: absolute; left: 0; width: 1200px; }
  .top-band { top: 0; height: 110px; }
  .bottom-wave { bottom: 0; height: 110px; }

  .website {
    position: absolute; right: 42px; top: 36px;
    color: var(--white); font-size: 22px; font-weight: 400; letter-spacing: 0.3px;
  }

  .brand {
    position: absolute; left: 47px; top: 70px; width: 532px;
    display: flex; flex-direction: column; align-items: center;
  }
  .brand-dot {
    width: 82px; height: 82px; border-radius: 50%;
    background: var(--sky-blue); margin-bottom: 14px;
  }
  .brand-name {
    color: var(--ink); font-weight: 400; font-size: 30px; line-height: 1.15; text-align: center;
  }

  .headline {
    position: absolute; left: 108px; top: 232px;
    color: var(--headline-blue); font-size: 145px; font-weight: 400; line-height: 1;
    letter-spacing: 0;
  }
  .tagline {
    position: absolute; left: 110px; top: 380px;
    color: var(--ink); font-size: 23px; font-weight: 600;
  }
  .services {
    position: absolute; left: 47px; top: 418px; width: 520px; text-align: center;
    color: var(--ink); font-size: 18px; font-weight: 400; line-height: 1.45;
  }

  .phone {
    position: absolute; left: 112px; top: 495px;
    color: var(--white); font-size: 36px; font-weight: 700;
  }

  .price-bubble { position: absolute; left: 556px; top: 306px; width: 240px; height: 250px; }
  .price-copy {
    position: absolute; left: 580px; top: 352px; width: 180px; text-align: center;
    transform: rotate(-7deg); color: #3a3a3a; font-weight: 600;
  }
  .price-copy .lead { font-size: 20px; line-height: 1.05; }
  .price-copy .lead-small { font-size: 17px; line-height: 1.05; }
  .price-copy .amount { font-size: 58px; font-weight: 700; color: var(--price-red); line-height: 1; letter-spacing: -1px; }
  .price-copy .extra { font-size: 18px; line-height: 1.1; }
</style>
</head>
<body>
<main class="postcard">
  <div class="scene-hillside" role="img" aria-label="Photo of a sunny Mediterranean hillside with cypress trees and the sea beyond"></div>
  <div class="scene-pool" role="img" aria-label="Photo of a sparkling blue infinity pool with tiled-roof gazebos and the sea behind"></div>

  <div class="intro-panel"></div>

  <svg class="top-band" viewBox="0 0 1200 110" preserveAspectRatio="none" aria-hidden="true">
    <defs>
      <linearGradient id="bandBlue" x1="0" y1="0" x2="1" y2="0">
        <stop offset="0" stop-color="#0292cd"/>
        <stop offset="0.6" stop-color="#1a7fc4"/>
        <stop offset="1" stop-color="#0555a3"/>
      </linearGradient>
    </defs>
    <path d="M0 0 H1200 V88 C1120 96 800 98 720 94 C650 90 640 30 575 28 H0 Z" fill="url(#bandBlue)"/>
  </svg>
  <div class="website">www.brightripplepoolcare.com.au</div>

  <div class="brand">
    <div class="brand-dot"></div>
    <div class="brand-name">Bright Ripple<br>Pool Care</div>
  </div>

  <h1 class="headline">RELEX</h1>
  <p class="tagline">and let us to take care of it for you</p>
  <p class="services">We also so one off,<br>weekly and fortnightly services as well</p>

  <svg class="bottom-wave" viewBox="0 0 1200 110" preserveAspectRatio="none" aria-hidden="true">
    <defs>
      <linearGradient id="waveGreen" x1="0" y1="0" x2="1" y2="0">
        <stop offset="0" stop-color="#0c7f36"/>
        <stop offset="0.5" stop-color="#1b9a45"/>
        <stop offset="1" stop-color="#22a64c"/>
      </linearGradient>
    </defs>
    <path d="M0 13 H560 C660 13 700 80 830 84 C960 88 1100 60 1200 44 V110 H0 Z" fill="url(#waveGreen)"/>
  </svg>
  <p class="phone">Phone: (02) 4813 2957</p>

  <svg class="price-bubble" viewBox="0 0 240 250" aria-hidden="true">
    <defs>
      <radialGradient id="bubbleRing" cx="0.4" cy="0.35" r="0.7">
        <stop offset="0" stop-color="#33a6d7"/>
        <stop offset="1" stop-color="#0555a3"/>
      </radialGradient>
      <radialGradient id="bubbleFace" cx="0.45" cy="0.4" r="0.65">
        <stop offset="0" stop-color="#ffffff"/>
        <stop offset="1" stop-color="#cfe4f4"/>
      </radialGradient>
    </defs>
    <path d="M112 8 A104 104 0 1 0 170 198 L190 240 L186 180 A104 104 0 0 0 112 8 Z" fill="url(#bubbleRing)"/>
    <circle cx="112" cy="112" r="88" fill="url(#bubbleFace)"/>
  </svg>
  <div class="price-copy">
    <div class="lead">Our monthly</div>
    <div class="lead-small">pool service is</div>
    <div class="amount">$67.00</div>
    <div class="extra">plus chemicals</div>
  </div>
</main>
</body>
</html>
```